we need a new logo and business card and package label for my cake business.
looking for a fresh and standout design.

i have attached my old card to this.

Industry/Entity Type

Hospitality

Contact Information for Business Card

Rosalind Tremaine
email: rosit07@mailvex.net
facebook:www.faceplaza.net/rosiesweetovens
mobile:0438127906

Logo Text

Desserts By Rosie T

Font styles to use
Decorative

Colors
ed2930
f04a51
b768aa
0356a4
33a6d7

Requirements
Must have
• standout design
• grab attention

```html
<!DOCTYPE html>
<html lang="en">
<head>
<meta charset="UTF-8">
<title>Desserts By Rosie T — Business Card</title>
<link href="https://fonts.googleapis.com/css2?family=Lato:wght@400;700&display=swap" rel="stylesheet">
<style>
  :root {
    --backdrop: #464646;
    --card: #ffffff;
    --red: #ed2930;
    --coral: #f04a51;
    --purple: #b768aa;
    --ink: #2b2b2b;
    --rule: #9a9a9a;
    --back-start: #b55fa6;
    --back-mid: #e5516a;
    --back-end: #b55fa6;
  }
  * { margin: 0; padding: 0; box-sizing: border-box; }
  html, body {
    width: 1200px; height: 900px; overflow: hidden;
    background: var(--backdrop);
    font-family: 'Lato', sans-serif;
  }
  .stage { position: relative; width: 1200px; height: 900px; }
  .card {
    position: absolute; top: 306px;
    width: 439px; height: 271px;
    border-radius: 10px; overflow: hidden;
  }
  .card-front { left: 149px; background: var(--card); }
  .card-back {
    left: 609px;
    background: linear-gradient(120deg, var(--back-start) 0%, var(--back-mid) 45%, var(--coral) 65%, var(--back-end) 100%);
  }
  .brand {
    position: absolute; left: 20px; top: 82px; width: 200px;
    text-align: center;
  }
  .brand-mark {
    display: block; margin: 0 auto 10px;
    width: 78px; height: 78px; border-radius: 50%;
    border: 4px solid var(--purple);
  }
  .brand-name {
    font-weight: 700; font-size: 19px; color: var(--red);
    white-space: nowrap;
  }
  .divider {
    position: absolute; left: 226px; top: 81px;
    width: 1px; height: 108px; background: var(--rule);
  }
  .details { position: absolute; left: 241px; top: 79px; }
  .person-name {
    font-weight: 700; font-size: 16px; letter-spacing: 0.2px;
    text-transform: uppercase; line-height: 1.1;
  }
  .person-name .first { color: var(--red); }
  .person-name .last { color: var(--purple); }
  .person-role { font-size: 12.5px; color: var(--ink); margin-top: 3px; }
  .contacts { list-style: none; margin-top: 24px; }
  .contacts li {
    display: flex; align-items: center; gap: 5px;
    font-size: 12.5px; color: var(--ink); height: 18.5px;
  }
  .contacts svg { width: 14px; height: 14px; flex: none; }
  .back-pattern { position: absolute; inset: 0; }
  .back-mark {
    position: absolute; left: 311px; top: 141px;
    width: 39px; height: 39px; border-radius: 50%;
    border: 2px solid #ffffff;
  }
</style>
</head>
<body>
<main class="stage">
  <section class="card card-front">
    <div class="brand">
      <span class="brand-mark"></span>
      <div class="brand-name">Desserts By Rosie T</div>
    </div>
    <div class="divider"></div>
    <div class="details">
      <h1 class="person-name"><span class="first">Rosalind</span> <span class="last">Tremaine</span></h1>
      <p class="person-role">Qualified Chef and Pastry Chef</p>
      <ul class="contacts">
        <li>
          <svg viewBox="0 0 14 14" aria-hidden="true"><circle cx="7" cy="7" r="7" fill="var(--red)"/><path d="M4 5.2 Q7 3.6 10 5.2 L9.4 6.4 L8.3 6 L8.3 5.3 Q7 4.9 5.7 5.3 L5.7 6 L4.6 6.4 Z M4.8 7 H9.2 L9.8 10 H4.2 Z" fill="#fff"/></svg>
          0438127906
        </li>
        <li>
          <svg viewBox="0 0 14 14" aria-hidden="true"><circle cx="7" cy="7" r="7" fill="var(--red)"/><rect x="3.6" y="4.6" width="6.8" height="4.8" fill="#fff"/><path d="M3.6 4.6 L7 7.3 L10.4 4.6" fill="none" stroke="var(--red)" stroke-width="0.8"/></svg>
          rosit07@mailvex.net
        </li>
        <li>
          <svg viewBox="0 0 14 14" aria-hidden="true"><circle cx="7" cy="7" r="7" fill="var(--red)"/></svg>
          /rosiesweetovens
        </li>
      </ul>
    </div>
  </section>

  <section class="card card-back">
    <div class="back-pattern" role="img" aria-label="Faint repeating pattern of the bakery emblem across the card back"></div>
    <span class="back-mark"></span>
  </section>
</main>
</body>
</html>
```